Electrician Company Website Design

I am looking to get a website designed only. I do not need it converted ot html. I simply need the design in a psd format. I have my own team for the conversion. The website is for an electrician company called Bramblecourt electric. I have created a txt document with the project parameters and specifics. I have also uploaded their logo in all avaible formats. It's a zip file.

Number of Pages Required

1 page

```html
<!DOCTYPE html>
<html lang="en">
<head>
<meta charset="utf-8">
<title>Bramblecourt Electric – Home</title>
<link href="https://fonts.googleapis.com/css2?family=Poppins:wght@400;500;600;700;800&display=swap" rel="stylesheet">
<style>
:root{
  --backdrop:#c9c9c9;
  --white:#ffffff;
  --ink:#111111;
  --muted:#555555;
  --blue:#1565c0;
  --red:#a3171c;
  --red-band:#c83a34;
  --dark:#2b2b2b;
  --hero-a:#1c2230;
  --hero-b:#3a3f47;
  --cream:#f1eeea;
  --rule:#e2e2e2;
}
*{margin:0;padding:0;box-sizing:border-box}
html,body{width:812px;height:1200px;overflow:hidden}
body{background:var(--backdrop);font-family:'Poppins',sans-serif;color:var(--ink);position:relative}
.page{position:absolute;left:214px;top:51px;width:384px;height:1098px;background:var(--white);overflow:hidden}
.abs{position:absolute}

/* header */
.header{left:0;top:0;width:384px;height:27px;background:var(--white);z-index:3}
.brand{left:48px;top:9px;display:flex;align-items:center;gap:3px;font-size:5.6px;font-weight:700;color:var(--ink);white-space:nowrap}
.brand-dot{width:7px;height:7px;border-radius:50%;background:var(--blue)}
.nav a{position:absolute;top:15px;font-size:4.3px;font-weight:500;color:var(--ink);text-decoration:none;white-space:nowrap}
.nav a.active{color:var(--red)}
.call{left:255px;top:0;width:80px;height:10px;background:var(--blue);color:var(--white);font-size:4.3px;font-weight:500;display:flex;align-items:center;justify-content:center;gap:2px}

/* hero */
.hero{left:0;top:27px;width:384px;height:141px;background:linear-gradient(100deg,var(--hero-a) 0%,#2a2f38 55%,var(--hero-b) 100%)}
.hero-kicker{left:48px;top:71px;font-size:4.3px;font-weight:600;color:var(--white)}
.hero-title{left:48px;top:77px;font-size:15.5px;line-height:17px;font-weight:800;color:var(--white);letter-spacing:-.2px}
.btn{display:flex;align-items:center;justify-content:center;background:var(--blue);color:var(--white);font-size:4.1px;font-weight:700;text-transform:uppercase}
.hero-btn{left:48px;top:116px;width:47px;height:13px}
.slider-arrow{top:156px;width:15px;height:12px;background:rgba(40,44,52,.85);display:flex;align-items:center;justify-content:center}

/* about */
.about-photo{left:48px;top:195px;width:140px;height:129px;background:linear-gradient(120deg,#c9a24a 0%,#6c7fa8 45%,#dcdde0 100%)}
.about-dots{left:168px;top:303px;width:32px;height:30px;background-image:radial-gradient(#9a9a9a .5px,transparent .6px);background-size:4px 4px}
.kicker{font-size:3.8px;font-weight:700;color:var(--red);text-transform:uppercase}
.about-kicker{left:205px;top:213px}
.h2{font-size:14.5px;line-height:15px;font-weight:600;color:var(--ink)}
.about-title{left:205px;top:220px;width:150px}
.body-copy{font-size:3.6px;line-height:6.7px;color:var(--muted)}
.about-copy{left:205px;top:254px;width:131px;text-align:justify}
.about-btn{left:205px;top:310px;width:47px;height:13px}

/* service band */
.band{left:0;top:356px;width:384px;height:145px;background:linear-gradient(180deg,#2e3340,#404550)}
.band svg{position:absolute;left:0;top:0}
.band-label{top:58px;font-size:9px;font-weight:600;color:var(--white);transform:translateX(-50%);white-space:nowrap}
.plus{width:13px;height:13px;border-radius:50%;background:var(--blue);border:1px solid var(--white);color:var(--white);font-size:6px;font-weight:600;display:flex;align-items:center;justify-content:center;transform:translateX(-50%)}
.band .plus{top:73px}

/* service areas */
.areas-title{left:48px;top:529px}
.areas-copy{left:48px;top:550px;width:120px}
.area-item{display:flex;align-items:center;gap:2px;font-size:3.9px;font-weight:600;white-space:nowrap}
.pin{width:9px;height:9px;border-radius:50%;background:var(--red);display:flex;align-items:center;justify-content:center}
.area-map{left:182px;top:534px;width:156px;height:95px;border-radius:12px;background:radial-gradient(ellipse at 50% 50%,#cfcfcf 0%,#e6e6e6 60%,#ffffff 100%)}

/* gallery */
.gallery-title{left:0;width:384px;top:657px;text-align:center}
.tile{width:70px;height:59px}
.tile-overlay{background:rgba(45,45,45,.82);display:flex;flex-direction:column;align-items:center;justify-content:center;gap:4px}
.tile-overlay span{font-size:5px;font-weight:600;color:var(--white)}
.tile-overlay .plus{position:static;transform:none;border:none}
.gallery-btn{left:157px;top:823px;width:69px;height:13px}

/* contact */
.contact{left:0;top:847px;width:384px;height:142px;background:var(--cream)}
.contact-card{left:48px;top:12px;width:151px;height:119px;background:var(--white)}
.contact-card h3{position:absolute;left:8px;top:10px;font-size:7.6px;font-weight:600}
.field{position:absolute;left:9px;width:134px;border-bottom:.5px solid var(--rule);font-size:3.6px;color:var(--muted);padding-bottom:2px}
.send-btn{left:9px;top:89px;width:33px;height:13px}
.contact-art{left:199px;top:0;width:185px;height:142px;background:radial-gradient(circle at 55% 45%,#f3b27a 0%,#e9d8c6 35%,var(--cream) 70%)}

/* footer */
.footer{left:0;top:989px;width:384px;height:109px;background:var(--dark);color:var(--white)}
.footer-brand{left:52px;top:16px;width:60px;display:flex;align-items:center;gap:3px;font-size:5px;font-weight:700;line-height:6px}
.footer-brand .brand-dot{flex:none}
.col-rule{top:13px;width:.7px;height:78px;background:#555}
.col-rule .tick{position:absolute;left:0;top:0;width:1.2px;height:10px;background:var(--white)}
.f-title{top:16px;font-size:5.4px;font-weight:700;text-transform:uppercase}
.f-text{font-size:4.3px;line-height:6.8px;color:#e6e6e6}
.f-links{left:213px;top:25px;list-style:none;font-size:3.9px;line-height:7.2px;color:#e6e6e6}
.social{top:24px;width:9px;height:9px;border-radius:50%;background:var(--white)}
.f-rule{left:0;top:91px;width:384px;height:.5px;background:#444}
.copyright{left:0;top:97px;width:384px;text-align:center;font-size:3.8px;color:#e6e6e6}
</style>
</head>
<body>
<main class="page">

  <header class="abs header">
    <div class="abs brand"><span class="brand-dot"></span>Bramblecourt Electric</div>
    <nav class="nav">
      <a class="active" style="left:154px">Home</a>
      <a style="left:177px">About Us</a>
      <a style="left:205px">Services</a>
      <a style="left:233px">Service Area</a>
      <a style="left:270px">Gallery</a>
      <a style="left:295px">FAQs</a>
      <a style="left:315px">Contact</a>
    </nav>
    <div class="abs call">
      <svg width="5" height="5" viewBox="0 0 10 10"><rect x=".7" y=".7" width="8.6" height="8.6" rx="1.5" fill="none" stroke="#fff" stroke-width="1"/><path d="M3 2.5l1 1.5-.6.7a4 4 0 0 0 1.9 1.9l.7-.6 1.5 1-.5 1C5 8 2 5 2 3z" fill="#fff"/></svg>
      Call us Now: 555 014 2290
    </div>
  </header>

  <section class="abs hero" role="img" aria-label="Electrician in hard hat and safety glasses working at a wired control panel"></section>
  <p class="abs hero-kicker">Bramblecourt Electric</p>
  <h1 class="abs hero-title">NOTHING IS<br>IMPOSSIBLE FOR US</h1>
  <a class="abs btn hero-btn">Learn More</a>
  <div class="abs slider-arrow" style="left:282px"><svg width="4" height="5" viewBox="0 0 4 6"><path d="M3 .5L1 3l2 2.5" fill="none" stroke="#fff" stroke-width=".8"/></svg></div>
  <div class="abs slider-arrow" style="left:299px"><svg width="4" height="5" viewBox="0 0 4 6"><path d="M1 .5L3 3l-2 2.5" fill="none" stroke="#fff" stroke-width=".8"/></svg></div>

  <section>
    <div class="abs about-dots"></div>
    <div class="abs about-photo" role="img" aria-label="Electrician in yellow helmet and mask testing a breaker panel with probes"></div>
    <p class="abs kicker about-kicker">About Us</p>
    <h2 class="abs h2 about-title">Professional Electrical Services</h2>
    <p class="abs body-copy about-copy">Lorem Ipsum is simply dummy text of the printing and typesetting industry. Lorem Ipsum has been the industry's standard dummy text ever since the 1500s, when an unknown printer took a galley of type and scrambled it to make a type specimen book. It has survived not only five centuries, but also the leap into electronic typesetting, remaining essentially unchanged. It was popularised in the 1960s with the release of Letraset sheets containing Lorem Ipsum passages.</p>
    <a class="abs btn about-btn">Learn More</a>
  </section>

  <section class="abs band" role="img" aria-label="Commercial office interior, residential wiring work and industrial plant">
    <svg width="384" height="145" viewBox="0 0 384 145">
      <rect x="0" y="0" width="110" height="145" fill="#3a4150"/>
      <rect x="237" y="0" width="147" height="145" fill="#4a4f58"/>
      <polygon points="99,0 237,0 274,145 136,145" fill="var(--red-band)"/>
    </svg>
    <span class="abs band-label" style="left:57px">Commerical</span>
    <span class="abs band-label" style="left:184px">Residential</span>
    <span class="abs band-label" style="left:316px">Industrial</span>
    <span class="abs plus" style="left:57px">+</span>
    <span class="abs plus" style="left:184px">+</span>
    <span class="abs plus" style="left:316px">+</span>
  </section>

  <section>
    <h2 class="abs h2 areas-title">Service areas</h2>
    <p class="abs body-copy areas-copy" style="font-size:4.3px;line-height:7.2px">Lorem Ipsum is simply dummy text of the printing and typesetting industry. Lorem Ipsum has been the industry's standard dummy text</p>
    <div class="abs area-item" style="left:48px;top:583px"><span class="pin"><svg width="4" height="5" viewBox="0 0 8 10"><path d="M4 0a3.5 3.5 0 0 0-3.5 3.5C.5 6 4 10 4 10s3.5-4 3.5-6.5A3.5 3.5 0 0 0 4 0z" fill="#fff"/><circle cx="4" cy="3.5" r="1.3" fill="#a3171c"/></svg></span>Lorem Ipsum</div>
    <div class="abs area-item" style="left:91px;top:583px"><span class="pin"><svg width="4" height="5" viewBox="0 0 8 10"><path d="M4 0a3.5 3.5 0 0 0-3.5 3.5C.5 6 4 10 4 10s3.5-4 3.5-6.5A3.5 3.5 0 0 0 4 0z" fill="#fff"/><circle cx="4" cy="3.5" r="1.3" fill="#a3171c"/></svg></span>Lorem Ipsum</div>
    <div class="abs area-item" style="left:134px;top:583px"><span class="pin"><svg width="4" height="5" viewBox="0 0 8 10"><path d="M4 0a3.5 3.5 0 0 0-3.5 3.5C.5 6 4 10 4 10s3.5-4 3.5-6.5A3.5 3.5 0 0 0 4 0z" fill="#fff"/><circle cx="4" cy="3.5" r="1.3" fill="#a3171c"/></svg></span>Lorem Ipsum</div>
    <div class="abs area-item" style="left:48px;top:596px"><span class="pin"><svg width="4" height="5" viewBox="0 0 8 10"><path d="M4 0a3.5 3.5 0 0 0-3.5 3.5C.5 6 4 10 4 10s3.5-4 3.5-6.5A3.5 3.5 0 0 0 4 0z" fill="#fff"/><circle cx="4" cy="3.5" r="1.3" fill="#a3171c"/></svg></span>Lorem Ipsum</div>
    <div class="abs area-item" style="left:91px;top:596px"><span class="pin"><svg width="4" height="5" viewBox="0 0 8 10"><path d="M4 0a3.5 3.5 0 0 0-3.5 3.5C.5 6 4 10 4 10s3.5-4 3.5-6.5A3.5 3.5 0 0 0 4 0z" fill="#fff"/><circle cx="4" cy="3.5" r="1.3" fill="#a3171c"/></svg></span>Lorem Ipsum</div>
    <div class="abs area-item" style="left:134px;top:596px"><span class="pin"><svg width="4" height="5" viewBox="0 0 8 10"><path d="M4 0a3.5 3.5 0 0 0-3.5 3.5C.5 6 4 10 4 10s3.5-4 3.5-6.5A3.5 3.5 0 0 0 4 0z" fill="#fff"/><circle cx="4" cy="3.5" r="1.3" fill="#a3171c"/></svg></span>Lorem Ipsum</div>
    <div class="abs area-item" style="left:48px;top:608px"><span class="pin"><svg width="4" height="5" viewBox="0 0 8 10"><path d="M4 0a3.5 3.5 0 0 0-3.5 3.5C.5 6 4 10 4 10s3.5-4 3.5-6.5A3.5 3.5 0 0 0 4 0z" fill="#fff"/><circle cx="4" cy="3.5" r="1.3" fill="#a3171c"/></svg></span>Lorem Ipsum</div>
    <div class="abs area-item" style="left:91px;top:608px"><span class="pin"><svg width="4" height="5" viewBox="0 0 8 10"><path d="M4 0a3.5 3.5 0 0 0-3.5 3.5C.5 6 4 10 4 10s3.5-4 3.5-6.5A3.5 3.5 0 0 0 4 0z" fill="#fff"/><circle cx="4" cy="3.5" r="1.3" fill="#a3171c"/></svg></span>Lorem Ipsum</div>
    <div class="abs area-item" style="left:134px;top:608px"><span class="pin"><svg width="4" height="5" viewBox="0 0 8 10"><path d="M4 0a3.5 3.5 0 0 0-3.5 3.5C.5 6 4 10 4 10s3.5-4 3.5-6.5A3.5 3.5 0 0 0 4 0z" fill="#fff"/><circle cx="4" cy="3.5" r="1.3" fill="#a3171c"/></svg></span>Lorem Ipsum</div>
    <div class="abs area-map" role="img" aria-label="Dotted world map with red location markers"></div>
  </section>

  <section>
    <h2 class="abs h2 gallery-title">Past Project Gallery</h2>
    <div class="abs tile" style="left:48px;top:685px;background:linear-gradient(135deg,#d9a46a,#e8c23a 50%,#c9c9c9)" role="img" aria-label="Electrician in yellow helmet at a panel"></div>
    <div class="abs tile" style="left:121px;top:685px;background:linear-gradient(135deg,#4a5a7a,#c58a6a 50%,#2d5da8)" role="img" aria-label="Hands wiring a distribution board"></div>
    <div class="abs tile" style="left:194px;top:685px;background:linear-gradient(180deg,#3d5a80,#d98a3a 60%,#f2b24a)" role="img" aria-label="Lineman on a pylon at sunset"></div>
    <div class="abs tile" style="left:266px;top:685px;background:linear-gradient(135deg,#2c3550,#6e86b0 60%,#b8c4d8)" role="img" aria-label="Technician in blue helmet with clipboard"></div>
    <div class="abs tile" style="left:48px;top:747px;background:linear-gradient(135deg,#d66a7a,#3a4a9a 50%,#1c2450)" role="img" aria-label="Close-up of industrial connectors"></div>
    <div class="abs tile tile-overlay" style="left:121px;top:747px" role="img" aria-label="Electrician at work, highlighted project">
      <span>Project Name Here</span><span class="plus">+</span>
    </div>
    <div class="abs tile" style="left:194px;top:747px;background:linear-gradient(135deg,#e9e4dc,#c7a88a 50%,#8a8a8a)" role="img" aria-label="Multimeter testing a breaker panel"></div>
    <div class="abs tile" style="left:266px;top:747px;background:linear-gradient(135deg,#5a6a7a,#d9c24a 55%,#e0e0d8)" role="img" aria-label="Engineer in hi-vis vest at a switch cabinet"></div>
    <a class="abs btn gallery-btn">View More Projects</a>
  </section>

  <section class="abs contact">
    <form class="abs contact-card">
      <h3>Send Us Message</h3>
      <div class="field" style="top:27px">Name</div>
      <div class="field" style="top:39px">Email</div>
      <div class="field" style="top:52px">Phone</div>
      <div class="field" style="top:72px">Message</div>
      <a class="abs btn send-btn">Send</a>
    </form>
    <div class="abs contact-art" role="img" aria-label="Illustrated electrician on a ladder fitting a hanging lamp"></div>
  </section>

  <footer class="abs footer">
    <div class="abs footer-brand"><span class="brand-dot"></span>Bramblecourt Electric</div>
    <div class="abs col-rule" style="left:120px"><span class="tick"></span></div>
    <div class="abs col-rule" style="left:204px"><span class="tick"></span></div>
    <div class="abs col-rule" style="left:276px"><span class="tick"></span></div>
    <h4 class="abs f-title" style="left:128px">Get in Touch</h4>
    <p class="abs f-text" style="left:128px;top:26px">1420 Alder Row<br>Fenwick, MN 55900</p>
    <p class="abs f-text" style="left:128px;top:43px">Phone :555 014 2290</p>
    <h4 class="abs f-title" style="left:211px">Sitemap</h4>
    <ul class="abs f-links">
      <li>Home</li><li>About Us</li><li>Services</li><li>Service Area</li><li>Gallery</li><li>FAQs</li><li>Contact</li>
    </ul>
    <h4 class="abs f-title" style="left:281px">Follow Us</h4>
    <span class="abs social" style="left:282px"></span>
    <span class="abs social" style="left:294px"></span>
    <div class="abs f-rule"></div>
    <p class="abs copyright">Copyright 2022 Bramblecourt Electric All Right Reserved</p>
  </footer>

</main>
</body>
</html>
```